K7 Digital Stationery Design Project

We are looking to have stationary designs created for our company branding materials. We are looking for the following to be created.
1. Business Cards (front & back)
2. Letterhead
3. Envelopes #10
We are a new web design, development and marketing firm. Primary color scheme is desired to be blue/grey/white. This web start-up is owned and operated by individuals with 15+ years experience each in the industry so should not look as though it is a start-up by young/inexperienced individuals.
We build website & custom applications/software. In addition we provide the full spectrum of web marketing solutions including SEO, PPC, Social Media, Branding, Content Marketing and PR.
Please let us know if you have any questions. Looking forward to seeing all the amazing design ideas.
Attached is our logo.
Thanks!
Target Market(s)
Company will be nearly 100% business to business sales. Looking to work with companies that are already established, with a website, who want to take their website and/or online marketing efforts to the next level.
Industry/Entity Type
Marketing
Look and feel

```html
<!DOCTYPE html>
<html lang="en">
<head>
<meta charset="utf-8">
<title>K7 Digital — Business Card</title>
<link rel="stylesheet" href="https://fonts.googleapis.com/css2?family=PT+Sans:wght@400;700&display=swap">
<style>
  :root {
    --stage: #e4e6e9;
    --card-white: #ffffff;
    --card-edge: #d7d9dc;
    --brand-blue: #1e8fd6;
    --blue-deep: #0d5f9a;
    --blue-light: #3aa6dd;
    --text-dark: #5a5a5a;
    --text-mid: #6e6e6e;
    --mark-grey: #e6e7e9;
    --mark-shade: #b9bbbe;
  }
  * { box-sizing: border-box; margin: 0; padding: 0; }
  html, body { width: 1200px; height: 871px; overflow: hidden; }
  body {
    background: var(--stage);
    font-family: "PT Sans", Verdana, sans-serif;
    display: flex;
    align-items: center;
    justify-content: center;
    gap: 40px;
  }
  .card {
    position: relative;
    width: 540px;
    height: 310px;
    border-radius: 22px;
    overflow: hidden;
    box-shadow: 0 10px 30px rgba(0,0,0,0.18);
  }
  /* Front */
  .card-front {
    background: linear-gradient(115deg, var(--card-white) 45%, #eceeef 100%);
    border: 1px solid var(--card-edge);
  }
  .front-decor-circle {
    position: absolute;
    right: -70px;
    top: 40px;
    width: 300px;
    height: 300px;
    border-radius: 50%;
    background: var(--mark-grey);
  }
  .front-edge-tab {
    position: absolute;
    right: 0;
    top: 200px;
    width: 16px;
    height: 52px;
    background: var(--mark-shade);
  }
  .front-content {
    position: absolute;
    left: 60px;
    top: 40px;
    width: 250px;
  }
  .brand {
    display: flex;
    align-items: center;
    justify-content: flex-end;
    gap: 8px;
  }
  .brand-dot {
    width: 14px;
    height: 14px;
    border-radius: 50%;
    background: var(--brand-blue);
  }
  .brand-name {
    font-size: 24px;
    font-weight: 700;
    color: var(--text-dark);
    letter-spacing: 0.5px;
    text-transform: uppercase;
  }
  .brand-tagline {
    text-align: right;
    font-size: 9px;
    color: var(--text-mid);
    margin-top: 2px;
  }
  .holder {
    margin-top: 20px;
    text-align: right;
  }
  .holder-name {
    font-size: 19px;
    font-weight: 700;
    color: var(--text-dark);
  }
  .holder-role {
    font-size: 13px;
    color: var(--text-mid);
  }
  .contact {
    list-style: none;
    margin-top: 14px;
    font-size: 12.5px;
    line-height: 1.35;
    color: var(--text-mid);
  }
  /* Back */
  .card-back {
    background: linear-gradient(135deg, var(--blue-light) 0%, var(--brand-blue) 45%, var(--blue-deep) 100%);
  }
  .back-decor-circle {
    position: absolute;
    right: -40px;
    top: -60px;
    width: 260px;
    height: 260px;
    border-radius: 50%;
    background: rgba(255,255,255,0.08);
  }
  .back-edge-tab {
    position: absolute;
    left: 0;
    top: 205px;
    width: 16px;
    height: 52px;
    background: rgba(255,255,255,0.25);
  }
  .back-brand {
    position: absolute;
    inset: 0;
    display: flex;
    align-items: center;
    justify-content: center;
    gap: 10px;
  }
  .back-brand .brand-dot { background: #ffffff; width: 16px; height: 16px; }
  .back-brand .brand-name { color: #ffffff; font-size: 30px; }
</style>
</head>
<body>
  <section class="card card-front" aria-label="Business card front">
    <div class="front-decor-circle"></div>
    <div class="front-edge-tab"></div>
    <div class="front-content">
      <div class="brand">
        <span class="brand-dot"></span>
        <span class="brand-name">K7 Digital</span>
      </div>
      <p class="brand-tagline">Web Design, Development and Marketing</p>
      <div class="holder">
        <p class="holder-name">Here your name</p>
        <p class="holder-role">Designation</p>
      </div>
      <ul class="contact">
        <li>123 street, City &amp; Country</li>
        <li>Phone : 88 123 123 123</li>
        <li>Cell : 88 123 123 123</li>
        <li>Fax : 88 123 123 123</li>
        <li>info@k7digital.com</li>
      </ul>
    </div>
  </section>

  <section class="card card-back" aria-label="Business card back">
    <div class="back-decor-circle"></div>
    <div class="back-edge-tab"></div>
    <div class="back-brand">
      <span class="brand-dot"></span>
      <span class="brand-name">K7 Digital</span>
    </div>
  </section>
</body>
</html>
```